Business Cards & Stationary for Law Firm using great new logo!
BrisvaleMoor LLC
Simple
Corinne T.Wexby, Esq.
712 Pruett Avenue
Larkfield, OR 97405
corinne.wexby@brisvalemoor-example.com
brisvalemoor-example.com
The front of the card should have the attorney name & email, the Firm name, address, phone, fax and website.
If the font used in the logo allows for lower case letters, please use the same font. BUT, if the font used in the logo requires all capitals (small caps and large caps), then please use standard fonts instead.
The logo design should be on the back of the card.
This is a higher resolution version of the logo. Please use this file going forward.

```html
<!DOCTYPE html>
<html lang="en">
<head>
<meta charset="utf-8">
<title>BrisvaleMoor LLC – Business Card</title>
<link href="https://fonts.googleapis.com/css2?family=Lato:ital,wght@0,400;1,400&display=swap" rel="stylesheet">
<style>
  :root {
    --page-bg: #e9eaee;
    --card-white: #ffffff;
    --brand-navy: #1f2f86;
    --brand-blue: #3f55b8;
    --swoosh-grey: #b9bcc6;
    --ink: #3a3d4a;
  }
  * { box-sizing: border-box; margin: 0; padding: 0; }
  html, body {
    width: 1200px; height: 980px; overflow: hidden;
    background: var(--page-bg);
  }
  .canvas {
    width: 1200px; height: 980px;
    display: flex; flex-direction: column;
    align-items: center; justify-content: center; gap: 38px;
  }
  .card {
    position: relative;
    width: 760px; height: 434px;
    background: var(--card-white);
    border-radius: 22px;
    overflow: hidden;
    box-shadow: 0 6px 20px rgba(30, 35, 60, 0.16);
  }
  .brand-name {
    font-family: "Lato", sans-serif;
    font-weight: 400;
    font-style: normal;
    color: var(--brand-navy);
    letter-spacing: 0.5px;
    white-space: nowrap;
  }
  .card-back .brand-name {
    position: absolute; left: 50%; top: 50%;
    transform: translate(-50%, -50%);
    font-size: 36px;
  }
  .card-front .brand-name {
    position: absolute; left: 50px; top: 54px;
    font-size: 28px;
  }
  .card-art {
    position: absolute; inset: 0;
    width: 100%; height: 100%;
  }
  .attorney-name {
    position: absolute; left: 50px; top: 146px;
    font-family: "Lato", sans-serif; font-style: italic;
    font-size: 17px; color: var(--ink);
  }
  .contact-list {
    position: absolute; left: 420px; top: 268px;
    list-style: none;
    font-family: "Lato", sans-serif; font-weight: 400;
    font-size: 11px; letter-spacing: 0.8px;
    text-transform: uppercase;
    color: var(--card-white);
  }
  .contact-list li {
    display: flex; align-items: center; gap: 10px;
    height: 23px;
  }
  .contact-icon {
    width: 15px; height: 15px; flex: none;
  }
  .contact-list .no-icon { padding-left: 25px; }
</style>
</head>
<body>
<main class="canvas">

  <section class="card card-back" aria-label="Card back">
    <span class="brand-name">BrisvaleMoor LLC</span>
  </section>

  <section class="card card-front" aria-label="Card front">
    <svg class="card-art" viewBox="0 0 760 434" preserveAspectRatio="none" aria-hidden="true">
      <defs>
        <linearGradient id="waveBlue" x1="0" y1="0" x2="1" y2="1">
          <stop offset="0" stop-color="#6f80d0"/>
          <stop offset="0.5" stop-color="#3f55b8"/>
          <stop offset="1" stop-color="#1f2f86"/>
        </linearGradient>
      </defs>
      <path d="M0,196 C220,214 420,330 760,128 L760,150 C430,350 210,238 0,222 Z" fill="#b9bcc6"/>
      <path d="M0,222 C210,238 430,350 760,150 L760,434 L0,434 Z" fill="url(#waveBlue)"/>
      <path d="M0,300 C240,330 470,400 760,260" fill="none" stroke="#8a98dc" stroke-width="2" opacity="0.5"/>
    </svg>

    <span class="brand-name">BrisvaleMoor LLC</span>
    <p class="attorney-name">Corinne T.Wexby, Esq.</p>

    <ul class="contact-list">
      <li>
        <svg class="contact-icon" viewBox="0 0 16 16"><circle cx="8" cy="8" r="8" fill="#fff"/><path d="M8 3.5a3 3 0 0 0-3 3c0 2.2 3 5.5 3 5.5s3-3.3 3-5.5a3 3 0 0 0-3-3zm0 4.2a1.2 1.2 0 1 1 0-2.4 1.2 1.2 0 0 1 0 2.4z" fill="#2c3f9e"/></svg>
        712 Pruett Avenue
      </li>
      <li class="no-icon">Larkfield, OR 97405</li>
      <li>
        <svg class="contact-icon" viewBox="0 0 16 16"><circle cx="8" cy="8" r="8" fill="#fff"/><path d="M5.5 4l1.5 0 .8 2-1 .8a5 5 0 0 0 2 2l.8-1 2 .8v1.5a1 1 0 0 1-1 1A6.5 6.5 0 0 1 4.5 5a1 1 0 0 1 1-1z" fill="#2c3f9e"/></svg>
        541.555.0148
      </li>
      <li>
        <svg class="contact-icon" viewBox="0 0 16 16"><circle cx="8" cy="8" r="8" fill="#fff"/><rect x="4.5" y="6" width="7" height="5" fill="#2c3f9e"/><rect x="6" y="4" width="4" height="2.5" fill="#2c3f9e"/></svg>
        541.555.0149
      </li>
      <li>
        <svg class="contact-icon" viewBox="0 0 16 16"><circle cx="8" cy="8" r="8" fill="#fff"/><rect x="4" y="5" width="8" height="6" fill="#2c3f9e"/><path d="M4 5l4 3.5L12 5" fill="none" stroke="#fff" stroke-width="0.9"/></svg>
        corinne.wexby@brisvalemoor-example.com
      </li>
      <li>
        <svg class="contact-icon" viewBox="0 0 16 16"><circle cx="8" cy="8" r="8" fill="#fff"/><circle cx="8" cy="8" r="4" fill="none" stroke="#2c3f9e" stroke-width="1.1"/><path d="M4 8h8M8 4c-2 2.5-2 5.5 0 8M8 4c2 2.5 2 5.5 0 8" fill="none" stroke="#2c3f9e" stroke-width="0.9"/></svg>
        brisvalemoor-example.com
      </li>
    </ul>
  </section>

</main>
</body>
</html>
```